Business Card, Stationery
Tax & Accounting Services
Professional
Lirena Vostrup EA
Tax Professional / Enrolled Agent
417 W Callory Avenue
Suite B
Bronx NY 10458
lvfiscalhub@quorvane.com
lvfiscalhub.com
Services:
Individual Tax Preparation
Business Tax Preparation
Tax Planning
DTB & State Tax Problems
Accounting
Payroll
Sales Tax
New Business Formation
Quickbooks Setup

```html
<!DOCTYPE html>
<html lang="en">
<head>
<meta charset="utf-8">
<title>LV Fiscal Hub Inc — Business Card</title>
<link rel="stylesheet" href="https://fonts.googleapis.com/css2?family=Cinzel:wght@500&family=Open+Sans:ital,wght@0,400;0,600;0,700;1,600&display=swap">
<style>
  :root {
    --bg: #e9e7e4;
    --card: #ffffff;
    --navy: #1f4a86;
    --blue: #2a63a8;
    --blue-light: #5b8fcb;
    --red: #c8202b;
    --ink: #3a3a3a;
    --grey: #6b6b6b;
    --rule: #b9b9b9;
  }
  * { box-sizing: border-box; margin: 0; padding: 0; }
  html, body { width: 1200px; height: 780px; overflow: hidden; background: var(--bg); }
  body { font-family: "Open Sans", Arial, sans-serif; position: relative; }

  .business-card {
    position: absolute; left: 60px; top: 81px;
    width: 1080px; height: 617px;
    background: var(--card);
    border-radius: 34px;
    overflow: hidden;
    box-shadow: 0 10px 30px rgba(0,0,0,.18);
  }
  .card-waves { position: absolute; inset: 0; width: 100%; height: 100%; }

  .brand { position: absolute; left: 150px; top: 118px; display: flex; align-items: center; gap: 18px; }
  .brand-square { width: 46px; height: 46px; background: var(--navy); }
  .brand-name { font-family: "Cinzel", Georgia, serif; font-weight: 500; font-size: 44px; color: var(--ink); letter-spacing: .5px; white-space: nowrap; }

  .holder { position: absolute; right: 572px; top: 278px; text-align: right; white-space: nowrap; }
  .holder-name { font-weight: 700; font-size: 29px; color: var(--navy); line-height: 1.2; }
  .holder-title { font-weight: 600; font-style: italic; font-size: 19px; color: var(--red); margin-top: 2px; }
  .holder-address { font-size: 20px; color: var(--grey); margin-top: 22px; line-height: 1.4; font-style: normal; }

  .divider { position: absolute; left: 532px; top: 262px; width: 1px; height: 178px; background: var(--rule); }

  .contact-list { position: absolute; left: 552px; top: 262px; list-style: none; }
  .contact-item { display: flex; align-items: center; gap: 12px; font-size: 19px; color: var(--grey); height: 36px; white-space: nowrap; }
  .contact-icon { width: 20px; height: 20px; flex: none; }
</style>
</head>
<body>
  <article class="business-card">
    <svg class="card-waves" viewBox="0 0 1080 617" aria-hidden="true">
      <defs>
        <linearGradient id="band-blue" x1="0" y1="0" x2="1" y2="0">
          <stop offset="0" stop-color="#1f4a86"/>
          <stop offset=".55" stop-color="#2f6db5"/>
          <stop offset="1" stop-color="#5b8fcb"/>
        </linearGradient>
      </defs>
      <path d="M0 575 C 320 630, 720 575, 1080 455 L1080 617 L0 617 Z" fill="url(#band-blue)"/>
      <path d="M0 520 C 320 600, 720 550, 1080 420 L1080 438 C 720 568, 320 615, 0 538 Z" fill="var(--red)"/>
    </svg>

    <header class="brand">
      <span class="brand-square"></span>
      <span class="brand-name">LV Fiscal Hub Inc</span>
    </header>

    <section class="holder">
      <h1 class="holder-name">Lirena Vostrup EA</h1>
      <p class="holder-title">Tax Professional / Enrolled Agent</p>
      <address class="holder-address">417 W Callory Avenue<br>Suite 4, Merrow NY 10982</address>
    </section>

    <div class="divider"></div>

    <ul class="contact-list">
      <li class="contact-item">
        <svg class="contact-icon" viewBox="0 0 20 20"><path d="M4 2 L8 2 L9 6 L7 8 C8 11 9 12 12 13 L14 11 L18 12 L18 16 C18 17 17 18 16 18 C8 18 2 12 2 4 C2 3 3 2 4 2 Z" fill="var(--red)"/></svg>
        <span>555-318-4402</span>
      </li>
      <li class="contact-item">
        <svg class="contact-icon" viewBox="0 0 20 20"><rect x="5" y="1" width="10" height="18" rx="2" fill="var(--red)"/><rect x="7" y="4" width="6" height="9" fill="#fff"/></svg>
        <span>555-207-6391</span>
      </li>
      <li class="contact-item">
        <svg class="contact-icon" viewBox="0 0 20 20"><rect x="5" y="2" width="10" height="6" fill="var(--grey)"/><rect x="2" y="7" width="16" height="9" rx="1.5" fill="var(--ink)"/><rect x="5" y="12" width="10" height="6" fill="#fff" stroke="var(--ink)"/></svg>
        <span>555-318-4403</span>
      </li>
      <li class="contact-item">
        <svg class="contact-icon" viewBox="0 0 20 20"><text x="10" y="15" text-anchor="middle" font-family="Open Sans, Arial, sans-serif" font-weight="700" font-size="16" fill="var(--ink)">@</text></svg>
        <span>lvfiscalhub@quorvane.com</span>
      </li>
      <li class="contact-item">
        <svg class="contact-icon" viewBox="0 0 20 20"><circle cx="10" cy="10" r="8" fill="var(--red)"/><path d="M2 10 H18 M10 2 C6 6 6 14 10 18 M10 2 C14 6 14 14 10 18" stroke="#fff" stroke-width="1.2" fill="none"/></svg>
        <span>www.lvfiscalhub.com</span>
      </li>
    </ul>
  </article>
</body>
</html>
```